PEACFUL ACUPUNCTURE PRACTITIONER NEEDS A NEW COAT

I need a new design for an exiting website http://stillwillowneedlework.example/ for a acupuncturist. This will be a minimalism design with lots and lots of white space. Home page and one interior page. Please keep the feeling of calm and peaceful serenity. For Color scheme: https://www.harborfernclinic.example/fertility. The bottom part of the home page with sections and links to the service pages: https://mossgatewellness.example/. The client likes this the best: http://qlhealing.example/. I'm attaching the logo and content pages.

Target Market(s)

Women

Industry/Entity Type

Wellness, health, wellbeing, meditation

Number of Pages Required

2 page

Font styles to use
Sans Serif
Decorative

Colors

Designer to choose colors to be used in the design.

Requirements
Must have
Nice to have
• Follow new website drafts and links
Should not have
• Busy with bright colors. No poping

```html
<!DOCTYPE html>
<html lang="en">
<head>
<meta charset="utf-8">
<title>Still Willow Acupuncture</title>
<link href="https://fonts.googleapis.com/css2?family=Josefin+Sans:wght@300;400;600&display=swap" rel="stylesheet">
<style>
:root{
  --rose-band:#e3cfd4;
  --rose-text:#b8898d;
  --rose-soft:#c39da0;
  --slate:#a7b5c5;
  --ink:#3a3536;
  --card:#f6f4f5;
  --line:#ececec;
  --white:#ffffff;
}
*{margin:0;padding:0;box-sizing:border-box}
html,body{width:818px;height:1200px;overflow:hidden;background:var(--white)}
body{position:relative;font-family:"Josefin Sans",sans-serif;color:var(--ink)}
.top-bar{position:absolute;left:0;top:0;width:818px;height:25px;background:var(--rose-band)}
.top-bar .email{position:absolute;left:110px;top:9px;font-size:7px;color:var(--white);letter-spacing:.1px}
.site-header{position:absolute;left:0;top:25px;width:818px;height:58px;border-bottom:1px solid var(--line);display:flex;align-items:center;justify-content:center;gap:7px}
.brand-dot{width:14px;height:14px;border-radius:50%;background:var(--rose-soft)}
.brand-name{font-size:14px;font-weight:400;color:#6d6264;letter-spacing:.3px}
.main-nav{position:absolute;left:110px;top:95px;width:594px;display:flex;justify-content:space-between;font-size:9px;font-weight:300;color:#4a4446;letter-spacing:.3px}
.hero{position:absolute;left:0;top:120px;width:818px;height:485px;overflow:hidden}
.hero-photo{position:absolute;inset:0;background:linear-gradient(90deg,#f6f2f3 0%,#f4eeee 30%,#ecd9d2 50%,#e2c2b1 70%,#dcb7a3 100%)}
.hero-title{position:absolute;left:112px;top:136px;font-size:33px;line-height:39px;font-weight:600;color:var(--rose-text);letter-spacing:.3px}
.hero-text{position:absolute;left:111px;top:233px;width:340px;font-size:10px;line-height:18.6px;font-weight:300;color:#2f2a2b}
.btn-contact{position:absolute;left:110px;top:314px;width:89px;height:34px;border-radius:17px;background:var(--slate);color:var(--white);font-size:8px;font-weight:400;display:flex;align-items:center;justify-content:center;letter-spacing:.2px}
.section-title{position:absolute;left:0;width:818px;text-align:center;font-size:27px;font-weight:400;color:var(--rose-text);letter-spacing:.5px}
.philosophy-title{top:654px}
.philosophy-text{position:absolute;left:110px;top:706px;width:598px;text-align:center;font-size:9px;line-height:17.5px;font-weight:300}
.philosophy-text p+p{margin-top:15px}
.divider{position:absolute;left:110px;top:835px;width:598px;height:1px;background:var(--line)}
.focus-title{top:886px}
.focus-grid{position:absolute;left:110px;top:946px;width:598px;height:169px;display:flex;gap:15.5px}
.focus-card{flex:1;background:var(--card);display:flex;flex-direction:column;align-items:center;padding-top:40px}
.focus-icon{width:64px;height:46px}
.focus-label{margin-top:14px;text-align:center;font-size:12.5px;line-height:16px;font-weight:300;color:var(--rose-soft)}
.icon-placeholder{width:64px;height:46px;border-radius:23px;background:linear-gradient(180deg,#e6eaf0,#dde3ea)}
.site-footer{position:absolute;left:0;top:1167px;width:818px;height:33px;background:var(--rose-band);display:flex;align-items:center;justify-content:center;font-size:7.5px;color:var(--white);font-weight:400}
</style>
</head>
<body>
<div class="top-bar"><span class="email">nora@stillwillowneedlework.example</span></div>

<header class="site-header">
  <span class="brand-dot"></span>
  <span class="brand-name">Still Willow Acupuncture</span>
</header>

<nav class="main-nav">
  <span>Home</span><span>About</span><span>Fertility &amp; Pregnancy</span><span>Hormone Balance</span><span>Strength &amp; Structure</span><span>Emotional Wellbeing</span><span>Online Shop</span><span>Testimonials</span>
</nav>

<section class="hero">
  <div class="hero-photo" role="img" aria-label="Soft-focus photo of acupuncture needles being placed on a relaxed client's shoulder"></div>
  <h1 class="hero-title">Welcome To<br>Still Willow</h1>
  <p class="hero-text">Lorem ipsum dolor sit amet, consectetur adipiscing elit, sed do mod eiusmod tempor incididunt ut labore et dolore magna aliqua nisi ut et aliquip ex ea commodo consequat.</p>
  <span class="btn-contact">CONTACT US</span>
</section>

<h2 class="section-title philosophy-title">Philosophy of Care</h2>
<div class="philosophy-text">
  <p>Acupuncture &amp; Chinese Herbal Medicine are rooted in over 3000 years of history and tradition. As a complete medical system that has remained flexible and relevant we honor what has worked from the past while embracing the medicine of tomorrow.</p>
  <p>At Still Willow Acupuncture we provide compassionate, respectful and empowering care in a safe &amp;inclusive environment. Our goal is to harmonize physical, mental and emotionalwellbeing to strengthen the Still Willow from which we all strive to live.</p>
</div>

<div class="divider"></div>

<h2 class="section-title focus-title">Areas of Focus</h2>
<div class="focus-grid">
  <div class="focus-card">
    <div class="icon-placeholder" role="img" aria-label="Line illustration of a nest with eggs"></div>
    <div class="focus-label">Fertility &amp;<br>Pregnancy</div>
  </div>
  <div class="focus-card">
    <svg class="focus-icon" viewBox="0 0 64 46" fill="none" stroke="#a7b5c5" stroke-width="1.6">
      <ellipse cx="32" cy="7" rx="12" ry="6"/>
      <ellipse cx="32" cy="19" rx="17" ry="6"/>
      <ellipse cx="32" cy="31" rx="15" ry="6"/>
      <ellipse cx="32" cy="41" rx="13" ry="4.5"/>
    </svg>
    <div class="focus-label">Hormone<br>Balance</div>
  </div>
  <div class="focus-card">
    <div class="icon-placeholder" role="img" aria-label="Line illustration of a tree"></div>
    <div class="focus-label">Strength &amp;<br>Structure</div>
  </div>
  <div class="focus-card">
    <svg class="focus-icon" viewBox="0 0 64 46" fill="none" stroke="#a7b5c5" stroke-width="1.6">
      <path d="M32 44 C18 32 12 24 12 14 C12 6 18 2 24 2 C28 2 31 5 32 8 C33 5 36 2 40 2 C46 2 52 6 52 14 C52 24 46 32 32 44 Z"/>
    </svg>
    <div class="focus-label">Emotional<br>Well-Being</div>
  </div>
</div>

<footer class="site-footer">Copyright © 2021 Still Willow Acupuncture | 14 Alder Row | Easton MA. 555-014-2290. All Rights Reserved.</footer>
</body>
</html>
```